Create our new Brightcup Coffee Syrup Label designs. A delicious job!

Design a front label for a range of coffee syrup flavours. The brand is 'Brightcup Coffee Syrups'. The flavours, vanilla, hazelnut and caramel.
Our coffee syrups are made with only natural colours and flavours and are positioned in the popular premium space in Australian and international cafes.
The labels will be applied to 750 ml Boston Bottles (see attached image).
Given that coffee syrups are often positioned in high visibility locations in cafes, they can be considered as objects of functional beauty.
This range is a sub brand for our company and I have attached our main brand images in the flavours we want. we want this brand to look different to this Marlowe branded range, but included the image to show what we are currently doing in this space.
The different flavours can be identified by a combination of colour and text, which may be a line or section of the otherwise same overall design.
We are going to do a 2 part label with the front just carrying Brand and flavour descriptors plus 750 ml.
Total Bottle height is 240 mm bottle width is 70 mm

Target Market(s)

Cafe patrons, primarily women, 18-35, Middle class in terms of economics, regular cafe patrons. Who are looking for a guilt free treat in their busy day.

Logo Text

Brightcup Coffee Syrups Vanilla (or Hazelnut, or Caramel) 750 ml

Logo styles of interest
Pictorial/Combination Logo
Font styles to use
Sans Serif

Colors

Designer to choose colors to be used in the design.

Requirements
Must have
• A clear design, which is a combination of font and image. it needs to be legible from up to 2m away (across a counter in a cafe).
• We would like to see a device, which may be a gold drop, that may be the 'brightcup' meant to the coffee.
• The way our coffee syrups are used is by adding a small amount (15 ml) to a cup
• of coffee, this adds both flavour and sweetness to the overall coffee experience, and cafes charge a premium for this service. We want our package to show this will be a great thing to do.
• We have a few options in terms of Label stock. We can print on a foil, that will allow a metallic sheen to come through the colours (see example of the Marlowe branded bottles.
Nice to have
• We are looking for a modern, clean and distinctive look and feel to this range.
• I have added a key line for the front and back label, however we can create a different label die line should the design warrant that. Note this is just for the front label.
Should not have
• Difficult to read fonts or imagery that is not clear.
• Should look different to the Marlowe branded product range.

```html
<!DOCTYPE html>
<html lang="en">
<head>
<meta charset="utf-8">
<title>Brightcup Coffee Syrup – Hazelnut Front Label</title>
<link rel="stylesheet" href="https://fonts.googleapis.com/css2?family=Open+Sans:wdth,wght@75..100,300..800&display=swap">
<style>
  :root {
    --label-black: #000000;
    --page-white: #ffffff;
    --keyline-copper: #b5652b;
    --text-white: #ffffff;
    --flavour-green: #62f00c;
    --drop-orange: #ff7a00;
  }
  * { margin: 0; padding: 0; box-sizing: border-box; }
  html, body {
    width: 764px;
    height: 1200px;
    overflow: hidden;
    background: var(--page-white);
  }
  .label {
    position: relative;
    width: 764px;
    height: 1200px;
    background: var(--label-black);
    border-radius: 40px;
    font-family: "Open Sans", sans-serif;
    color: var(--text-white);
    text-align: center;
  }
  .keyline {
    position: absolute;
    inset: 0;
  }
  .brand {
    position: absolute;
    left: 0;
    right: 0;
    top: 160px;
    font-weight: 400;
    color: var(--text-white);
    line-height: 1;
  }
  .brand-name {
    display: block;
    font-size: 66px;
    letter-spacing: 0.01em;
  }
  .brand-line {
    display: block;
    margin-top: 22px;
    font-size: 48px;
    letter-spacing: 0.06em;
  }
  .brand-dot {
    display: inline-block;
    width: 22px;
    height: 22px;
    border-radius: 50%;
    background: var(--drop-orange);
    margin-left: 12px;
    vertical-align: 4px;
  }
  .claims {
    position: absolute;
    left: 0;
    right: 0;
    top: 535px;
    font-size: 35px;
    font-weight: 600;
    letter-spacing: 0.13em;
    line-height: 46px;
  }
  .flavour {
    position: absolute;
    left: 0;
    right: 0;
    top: 812px;
    color: var(--flavour-green);
    font-stretch: 75%;
    line-height: 1;
  }
  .flavour-name {
    display: block;
    font-size: 86px;
    font-weight: 800;
  }
  .flavour-type {
    display: block;
    margin-top: 4px;
    font-size: 86px;
    font-weight: 400;
  }
  .net-volume {
    position: absolute;
    left: 0;
    right: 0;
    top: 1097px;
    font-size: 19px;
    font-weight: 400;
    letter-spacing: -0.01em;
  }
</style>
</head>
<body>
  <main class="label">
    <svg class="keyline" width="764" height="1200" viewBox="0 0 764 1200" aria-hidden="true">
      <rect x="35" y="35" width="694" height="1130" rx="28" ry="28"
            fill="none" stroke="var(--keyline-copper)" stroke-width="1.2"
            stroke-dasharray="16 12"/>
    </svg>

    <h1 class="brand">
      <span class="brand-name">BRIGHTCUP<span class="brand-dot"></span></span>
      <span class="brand-line">COFFEE SYRUP</span>
    </h1>

    <p class="claims">NATURAL FLAVOURS<br>NATURAL COLOURS</p>

    <h2 class="flavour">
      <span class="flavour-name">HAZELNUT</span>
      <span class="flavour-type">SYRUP</span>
    </h2>

    <p class="net-volume">NET WT: 750 ML</p>
  </main>
</body>
</html>
```